Company Truck Wrap Design

Truck wrap design. Would like the company logo to look 3d if possible and incorporate blue in the design in with the orange of the logo.

```html
<!DOCTYPE html>
<html lang="en">
<head>
<meta charset="utf-8">
<title>Keystone Roofing and Contracting – Truck Wrap</title>
<link rel="stylesheet" href="https://fonts.googleapis.com/css2?family=Oswald:wght@700&family=Roboto+Condensed:wght@700&display=swap">
<style>
  :root {
    --brand-orange: #f07a1f;
    --deep-orange: #e8621a;
    --royal-blue: #1f3fd6;
    --bright-blue: #2c7be8;
    --sky-blue: #5cb4f0;
    --lavender: #c9c6ea;
    --roof-purple: #8a6f8c;
    --roof-grey: #9aa3a8;
    --white: #ffffff;
  }
  * { margin: 0; padding: 0; box-sizing: border-box; }
  html, body { width: 1200px; height: 435px; overflow: hidden; background: var(--white); }
  .wrap-panel { position: relative; width: 1200px; height: 435px; background: var(--white); overflow: hidden; }
  .bed-graphics { position: absolute; inset: 0; }
  .brand-block {
    position: absolute; left: 28px; top: 100px; width: 340px;
    font-family: "Roboto Condensed", sans-serif; font-weight: 700;
    color: var(--brand-orange); text-align: center;
  }
  .brand-name { font-size: 70px; line-height: 1; letter-spacing: 1px; }
  .brand-tagline { font-size: 30px; line-height: 1.2; margin-top: 4px; }
  .certifications {
    position: absolute; left: 52px; top: 300px; width: 300px;
    display: flex; justify-content: space-between;
  }
  .cert-badge { width: 70px; height: 70px; border-radius: 50%; }
  .cert-badge.inspector { background: var(--sky-blue); }
  .cert-badge.tile { background: #e9e4d6; border: 4px solid #8a6a3a; }
  .cert-badge.licensed { background: #1a1a1a; border: 4px solid #ffffff; box-shadow: 0 0 0 2px #1a1a1a; }
  .service-title {
    position: absolute; left: 552px; top: 128px;
    font-family: "Oswald", sans-serif; font-weight: 700;
    color: var(--royal-blue); font-size: 42px; line-height: 1;
    text-transform: uppercase; white-space: nowrap;
    transform: rotate(-22deg); transform-origin: left top;
  }
  .service-title .line-one { display: block; margin-left: 44px; }
  .service-title .line-two { display: block; }
</style>
</head>
<body>
<main class="wrap-panel">
  <svg class="bed-graphics" width="1200" height="435" viewBox="0 0 1200 435">
    <defs>
      <linearGradient id="bedWash" x1="0" x2="1" y1="0" y2="0">
        <stop offset="0" stop-color="#ffffff"/>
        <stop offset="1" stop-color="#c9c6ea"/>
      </linearGradient>
      <linearGradient id="roofTiles" x1="0" x2="1" y1="0" y2="0">
        <stop offset="0" stop-color="#9aa3a8"/>
        <stop offset="0.5" stop-color="#b8b0c4"/>
        <stop offset="1" stop-color="#8a6f8c"/>
      </linearGradient>
      <linearGradient id="workerFill" x1="0" x2="0" y1="0" y2="1">
        <stop offset="0" stop-color="#f3b53a"/>
        <stop offset="0.45" stop-color="#d8413a"/>
        <stop offset="0.8" stop-color="#2f6fd0"/>
        <stop offset="1" stop-color="#e58a2a"/>
      </linearGradient>
      <linearGradient id="blueSweep" x1="0" x2="1" y1="0" y2="1">
        <stop offset="0" stop-color="#1f3fd6"/>
        <stop offset="0.6" stop-color="#2c7be8"/>
        <stop offset="1" stop-color="#1f3fd6"/>
      </linearGradient>
    </defs>
    <polygon class="bed-wash" points="385,0 800,0 680,435 385,435" fill="url(#bedWash)"/>
    <rect class="worker-illustration" role="img" aria-label="Cartoon roofer in hard hat and overalls giving a thumbs up, with a fiery swoosh at his feet" x="388" y="10" width="145" height="415" rx="18" fill="url(#workerFill)" opacity="0.85"/>
    <polygon class="roof-photo" role="img" aria-label="Photo of a tiled roof with battens" points="800,0 1010,0 930,435 680,435" fill="url(#roofTiles)"/>
    <polygon class="accent-line" points="792,0 802,0 684,435 674,435" fill="var(--brand-orange)"/>
    <polygon class="blue-field" points="1010,0 1200,0 1200,435 930,435" fill="url(#blueSweep)"/>
    <polygon class="blue-highlight" points="1120,0 1170,0 1040,435 990,435" fill="var(--sky-blue)" opacity="0.5"/>
    <polygon class="orange-stripe" points="1030,0 1042,0 968,300 956,300" fill="var(--brand-orange)"/>
    <polygon class="orange-stripe" points="1060,0 1072,0 990,320 978,320" fill="var(--brand-orange)"/>
    <polygon class="orange-corner" points="1200,250 1200,435 1010,435" fill="var(--brand-orange)"/>
  </svg>

  <div class="brand-block">
    <div class="brand-name">KEYSTONE</div>
    <div class="brand-tagline">Roofing and Contracting</div>
  </div>

  <div class="certifications">
    <div class="cert-badge inspector"></div>
    <div class="cert-badge tile"></div>
    <div class="cert-badge licensed"></div>
  </div>

  <div class="service-title">
    <span class="line-one">Roofing</span>
    <span class="line-two">&amp; Contracting</span>
  </div>
</main>
</body>
</html>
```